Brochure & Business card design

Looking for a new business card design i want it to be modern and sharp looking i usually order plastic business cards, and i would like to make the colors like the logo teal/charcoal i will like to have our services on icons with words.... our services are
ROOFING GUTTERS PAINTING PRESSURE WASHING EXTERIOR DESIGN & ATTIC VENTILATION. I also want to add my credentials

Target Market(s)

Oregon local market

Industry/Entity Type

Residential Construction

Contact Information for Business Card

Business info, services, number, website

Font styles to use
Serif
Sans Serif

Colors
33b8a4
5c5c5c
ffffff

Requirements
Must have
• Dale Finch
• Cell:
• Office:
• Email:
• Website:
• also i need our social media icons
• Services ROOFING GUTTERS PAINTING PRESSURE WASHING EXTERIOR DESIGN & ATTIC VENTILATION
• -icons for number, web, email, cell
• OR #584312
• Wa #KTRABLD461X7
Nice to have
• -Clean design Front & Back
• -Icons
• -shape House just like logo design
• -First Impression
Should not have
• Not Busy or lost of eye contact

```html
<!DOCTYPE html>
<html lang="en">
<head>
<meta charset="utf-8">
<title>Ridgeline Exteriors – Business Card</title>
<link rel="stylesheet" href="https://fonts.googleapis.com/css2?family=Arimo:wght@400;700&display=swap">
<style>
  :root {
    --teal: #13998a;
    --charcoal: #4a4a4c;
    --paper: #f4f4f3;
    --white: #ffffff;
    --backdrop: #e4e4e4;
  }
  * { box-sizing: border-box; margin: 0; padding: 0; }
  html, body {
    width: 1200px; height: 1200px; overflow: hidden;
    background: var(--backdrop);
    font-family: "Arimo", Arial, sans-serif;
  }
  .canvas { position: relative; width: 1200px; height: 1200px; }
  .card {
    position: absolute; left: 150px; width: 900px; height: 514px;
    box-shadow: 0 6px 18px rgba(0,0,0,0.12);
    overflow: hidden;
  }
  /* Back side */
  .card--back { top: 50px; background: var(--teal); }
  .back-brand {
    position: absolute; left: 0; right: 0; top: 200px;
    display: flex; align-items: center; justify-content: center; gap: 16px;
  }
  .brand-mark { width: 28px; height: 28px; background: var(--white); }
  .back-name { color: var(--white); font-weight: 700; font-size: 44px; letter-spacing: 1px; }
  .back-web {
    position: absolute; left: 0; right: 0; top: 275px; text-align: center;
    color: var(--white); font-size: 18px;
  }
  /* Front side */
  .card--front { top: 636px; background: var(--paper); }
  .front-brand {
    position: absolute; left: 0; right: 0; top: 100px;
    display: flex; align-items: center; justify-content: center; gap: 16px;
  }
  .front-brand .brand-mark { background: var(--teal); }
  .front-name { color: var(--teal); font-weight: 700; font-size: 44px; letter-spacing: 1px; }
  .info-band {
    position: absolute; left: 0; right: 0; top: 240px; bottom: 0;
    background: var(--teal);
  }
  .band-notch { position: absolute; left: 148px; top: 228px; }
  .person { position: absolute; left: 108px; top: 256px; color: var(--white); }
  .person-name { font-size: 33px; font-weight: 700; }
  .person-title { font-size: 18px; margin-top: 2px; }
  .credentials { margin-top: 14px; font-size: 15px; line-height: 22px; }
  .social { display: flex; gap: 10px; margin-top: 16px; }
  .social-dot {
    width: 26px; height: 26px; border-radius: 50%;
    border: 2px solid var(--white);
  }
  .contacts {
    position: absolute; left: 480px; top: 262px; list-style: none; color: var(--white);
  }
  .contact {
    display: flex; align-items: center; height: 36px; font-size: 17px;
  }
  .contact svg { width: 24px; height: 24px; margin-right: 20px; flex: none; }
  .contact-label { width: 62px; font-weight: 700; font-size: 15px; }
  .services {
    position: absolute; left: 0; right: 0; bottom: 12px;
    display: flex; justify-content: center; gap: 16px;
    list-style: none; color: var(--white); font-size: 13px; letter-spacing: 0.2px;
  }
  .service { display: flex; align-items: center; gap: 6px; white-space: nowrap; }
  .service svg { width: 16px; height: 16px; flex: none; }
</style>
</head>
<body>
<main class="canvas">
  <section class="card card--back" aria-label="Card back">
    <div class="back-brand">
      <span class="brand-mark"></span>
      <span class="back-name">RIDGELINE EXTERIORS</span>
    </div>
    <p class="back-web">www.ridgelineext.com</p>
  </section>

  <section class="card card--front" aria-label="Card front">
    <div class="front-brand">
      <span class="brand-mark"></span>
      <span class="front-name">RIDGELINE EXTERIORS</span>
    </div>

    <div class="info-band"></div>
    <svg class="band-notch" width="30" height="13" viewBox="0 0 30 13">
      <polygon points="0,12 15,0 30,12" fill="#13998a"/>
    </svg>

    <div class="person">
      <p class="person-name">Dale Finch</p>
      <p class="person-title">CEO</p>
      <p class="credentials">OR #584312<br>WA #KTRABLD461X7</p>
      <div class="social" aria-label="Social media">
        <span class="social-dot"></span>
        <span class="social-dot"></span>
        <span class="social-dot"></span>
      </div>
    </div>

    <ul class="contacts">
      <li class="contact">
        <svg viewBox="0 0 24 24"><rect x="6" y="2" width="12" height="20" rx="2" fill="none" stroke="#fff" stroke-width="2"/><line x1="10" y1="18" x2="14" y2="18" stroke="#fff" stroke-width="2"/></svg>
        <span class="contact-label">Cell:</span><span>061947235</span>
      </li>
      <li class="contact">
        <svg viewBox="0 0 24 24"><path fill="#fff" d="M6.6 10.8a15.1 15.1 0 0 0 6.6 6.6l2.2-2.2a1 1 0 0 1 1-.25 11.4 11.4 0 0 0 3.6.57 1 1 0 0 1 1 1V20a1 1 0 0 1-1 1A17 17 0 0 1 3 4a1 1 0 0 1 1-1h3.5a1 1 0 0 1 1 1c0 1.25.2 2.45.57 3.6a1 1 0 0 1-.25 1z"/></svg>
        <span class="contact-label">Office:</span><span>061947236</span>
      </li>
      <li class="contact">
        <svg viewBox="0 0 24 24"><rect x="2" y="6" width="20" height="14" fill="none" stroke="#fff" stroke-width="2"/><polyline points="2,6 12,14 22,6" fill="none" stroke="#fff" stroke-width="2"/></svg>
        <span class="contact-label">Email:</span><span>hello@ridgelineext.com</span>
      </li>
      <li class="contact">
        <svg viewBox="0 0 24 24"><path fill="#fff" d="M12 2a7 7 0 0 0-7 7c0 5 7 12 7 12s7-7 7-12a7 7 0 0 0-7-7zm0 9.5A2.5 2.5 0 1 1 12 6.5a2.5 2.5 0 0 1 0 5z"/></svg>
        <span class="contact-label">Office:</span><span>48 Alder Lane, Salem</span>
      </li>
      <li class="contact">
        <svg viewBox="0 0 24 24"><circle cx="12" cy="12" r="9" fill="none" stroke="#fff" stroke-width="1.8"/><ellipse cx="12" cy="12" rx="4" ry="9" fill="none" stroke="#fff" stroke-width="1.5"/><line x1="3" y1="12" x2="21" y2="12" stroke="#fff" stroke-width="1.5"/></svg>
        <span class="contact-label">Web:</span><span>www.ridgelineext.com</span>
      </li>
    </ul>

    <ul class="services">
      <li class="service"><svg viewBox="0 0 16 16"><polyline points="1,9 8,2 15,9" fill="none" stroke="#fff" stroke-width="2"/></svg>ROOFING</li>
      <li class="service"><svg viewBox="0 0 16 16"><path d="M2 4v6h12V4" fill="none" stroke="#fff" stroke-width="2"/></svg>GUTTERS</li>
      <li class="service"><svg viewBox="0 0 16 16"><rect x="2" y="2" width="12" height="5" fill="#fff"/><line x1="8" y1="7" x2="8" y2="15" stroke="#fff" stroke-width="2"/></svg>PAINTING</li>
      <li class="service"><svg viewBox="0 0 16 16"><circle cx="8" cy="8" r="6" fill="none" stroke="#fff" stroke-width="2"/></svg>PRESSURE WASHING</li>
      <li class="service"><svg viewBox="0 0 16 16"><polygon points="8,1 15,7 15,15 1,15 1,7" fill="none" stroke="#fff" stroke-width="2"/></svg>EXTERIOR DESIGN</li>
      <li class="service"><svg viewBox="0 0 16 16"><polygon points="8,2 15,14 1,14" fill="none" stroke="#fff" stroke-width="2"/></svg>ATTIC VENTILATION</li>
    </ul>
  </section>
</main>
</body>
</html>
```